Business card/ stationery for chemical distributor company
Novaryn Chemicals Co., Ltd.
Business card/ stationery for chemical distributor company - Chemicals
Creative Brief
Simple
Wen Liao
Business Manager
7F, 3, Sec. 2, Heping W. Rd., Taipei 10672, Taiwan
This column is not cecessary
TBD(48201736)
info@novaryn.com.tw
www.novaryn.com.tw
no
I need double sided standard business. However I need only ''one design'' for both side. One side is designed in English as standard and the other side I will translate it into Chinese by myself. So please leave design only. For the design, simple, clear and looks professional is enough. Don't need to be too fancy and complicated. :)
Use the same design for both side. For the side in Chinease, reserved the column and design and please leave the information blank.

```html
<!DOCTYPE html>
<html lang="en">
<head>
<meta charset="utf-8">
<title>Novaryn Chemicals – Stationery</title>
<link href="https://fonts.googleapis.com/css2?family=Open+Sans:wght@400;600&display=swap" rel="stylesheet">
<style>
:root{
  --bg:#222223;
  --paper:#ffffff;
  --orange:#f26b21;
  --orange-light:#f7931e;
  --grey:#6d6e70;
  --grey-light:#9a9a9c;
  --ink:#3a3a3c;
  --flap:#ebebec;
}
*{margin:0;padding:0;box-sizing:border-box}
html,body{width:1200px;height:614px;overflow:hidden;background:var(--bg)}
body{position:relative;font-family:"Open Sans",Arial,sans-serif;color:var(--grey)}
.sheet{position:absolute;background:var(--paper);overflow:hidden}
.abs{position:absolute}
.wordmark{position:absolute;display:flex;align-items:center;gap:5px;font-weight:600;color:var(--grey);letter-spacing:.3px;line-height:1}
.wordmark .dot{display:block;background:var(--orange)}
.name{color:var(--orange);font-weight:600;line-height:1}
.role{color:var(--grey-light);line-height:1}
.lines{line-height:1.35}
.contact{list-style:none}
.contact li{display:flex;align-items:center;gap:3px;white-space:nowrap}
.contact svg{width:6px;height:6px;fill:var(--grey);flex:none}
.contact.orange-icons svg{fill:var(--orange)}
.accent{position:absolute;background:linear-gradient(var(--orange-light),var(--orange))}

/* business cards */
.card{width:241px;height:138px;left:25px}
.card-front-a{top:129px}
.card-front-b{top:286px}
.card-back{top:443px}
.card .wordmark{left:24px;top:61px;font-size:19px}
.card .wordmark .dot{width:11px;height:11px}
.card .info{left:142px;top:26px;font-size:5.3px}
.card .info .name{font-size:8.5px;text-transform:uppercase}
.card .info .role{font-size:5.8px;margin-top:2px}
.card .info .lines{margin-top:4px}
.card .info .contact{margin-top:5px;line-height:1.65}
.card-front-b .band{position:absolute;left:0;bottom:0;height:3px;width:100%;
  background:linear-gradient(90deg,var(--orange) 0,var(--orange-light) 63%,var(--grey-light) 63%,var(--grey-light) 100%)}
.card-back .wordmark{left:13px;top:20px;font-size:22px}
.card-back .wordmark .dot{width:13px;height:13px}
.card-back .address{left:13px;top:63px;font-size:5.3px}
.card-back .contact{left:13px;top:84px;font-size:5.3px;line-height:1.65}
.card-back .sign{right:13px;top:88px;text-align:right}
.card-back .sign .name{font-size:8.5px}
.card-back .sign .role{font-size:5.8px;margin-top:2px}
.card-back .accent{right:0;top:84px;width:4px;height:20px}

/* letterhead */
.letterhead{left:289px;top:25px;width:396px;height:558px}
.letterhead .accent{top:40px;width:3px;height:44px}
.letterhead .accent.left{left:0}
.letterhead .accent.right{right:0}
.letterhead .wordmark{left:26px;top:54px;font-size:20px}
.letterhead .wordmark .dot{width:12px;height:12px}
.letterhead .address{right:115px;top:52px;text-align:right;font-size:5.6px;line-height:1.55}
.letterhead .address .web{color:var(--orange);letter-spacing:.6px}
.letterhead .divider{left:290px;top:45px;width:.6px;height:38px;background:#cfcfcf}
.letterhead .contact{left:299px;top:46px;font-size:5.6px;line-height:1.75}
.letter{left:25px;top:178px;width:340px;font-size:6.3px;color:var(--ink);line-height:1.38}
.letter p{margin-bottom:7.5px}
.letter .greeting{margin-bottom:17px}
.letter .sign .name{font-size:8.5px;margin-top:1px}
.letter .sign .role{font-size:5.8px;margin-top:2px}

/* envelopes */
.envelope-back{left:705px;top:149px;width:466px;height:209px}
.envelope-back .flap{left:0;top:0;width:466px;height:80px}
.envelope-back .wordmark{left:50%;transform:translateX(-50%);top:30px;font-size:12px}
.envelope-back .wordmark .dot{width:8px;height:8px}
.envelope-back .web{left:0;right:0;top:56px;text-align:center;font-size:5.4px;color:var(--orange);letter-spacing:.6px}
.envelope-front{left:705px;top:377px;width:466px;height:208px}
.envelope-front .accent{left:0;top:15px;width:4px;height:57px}
.envelope-front .wordmark{left:18px;top:26px;font-size:20px}
.envelope-front .wordmark .dot{width:12px;height:12px}
.envelope-front .address{left:29px;top:58px;font-size:5.6px;line-height:1.55}
</style>
</head>
<body>
<svg width="0" height="0" style="position:absolute" aria-hidden="true">
  <defs>
    <symbol id="i-phone" viewBox="0 0 10 10"><path d="M1 4c0-2 2-3 4-3s4 1 4 3H7V3H3v1zM2 5h6l1 4H1z"/></symbol>
    <symbol id="i-mobile" viewBox="0 0 10 10"><path d="M3 0h4a1 1 0 0 1 1 1v8a1 1 0 0 1-1 1H3a1 1 0 0 1-1-1V1a1 1 0 0 1 1-1zm0 1.5v6.5h4V1.5z"/></symbol>
    <symbol id="i-fax" viewBox="0 0 10 10"><path d="M3 0h4v3H3zM1 4h8v4H7v2H3V8H1zm3 3v2h2V7z"/></symbol>
    <symbol id="i-mail" viewBox="0 0 10 10"><path d="M0 2h10v6H0zm1 1v.4l4 2.4 4-2.4V3z"/></symbol>
    <symbol id="i-web" viewBox="0 0 10 10"><path d="M5 0a5 5 0 1 0 0 10A5 5 0 0 0 5 0zm0 1.2c.7.8 1.1 2 1.2 3.3H3.8C3.9 3.2 4.3 2 5 1.2zM3.8 5.5h2.4C6.1 6.8 5.7 8 5 8.8 4.3 8 3.9 6.8 3.8 5.5zM1.2 4.5A3.9 3.9 0 0 1 3.4 1.5 6 6 0 0 0 2.8 4.5zm0 1h1.6c.1 1.1.3 2.2.6 3A3.9 3.9 0 0 1 1.2 5.5zm6 0h1.6a3.9 3.9 0 0 1-2.2 3c.3-.8.5-1.9.6-3zm0-1a6 6 0 0 0-.6-3 3.9 3.9 0 0 1 2.2 3z"/></symbol>
  </defs>
</svg>

<!-- Business card, front -->
<section class="sheet card card-front-a">
  <div class="wordmark"><span class="dot"></span>Novaryn</div>
  <div class="abs info">
    <div class="name">Wen Liao</div>
    <div class="role">Business Manager</div>
    <div class="lines">7F, 3, Sec. 2, Heping W. Rd.<br>Taipei 10672, Taiwan</div>
    <ul class="contact">
      <li><svg><use href="#i-phone"/></svg>127 482 0173</li>
      <li><svg><use href="#i-mobile"/></svg>345 482 0173</li>
      <li><svg><use href="#i-fax"/></svg>345 482 0173</li>
      <li><svg><use href="#i-mail"/></svg>info@novaryn.com.tw</li>
      <li><svg><use href="#i-web"/></svg>www.novaryn.com.tw</li>
    </ul>
  </div>
</section>

<!-- Business card, front with band -->
<section class="sheet card card-front-b">
  <div class="wordmark"><span class="dot"></span>Novaryn</div>
  <div class="abs info">
    <div class="name">Wen Liao</div>
    <div class="role">Business Manager</div>
    <div class="lines">7F, 3, Sec. 2, Heping W. Rd.<br>Taipei 10672, Taiwan</div>
    <ul class="contact">
      <li><svg><use href="#i-phone"/></svg>127 482 0173</li>
      <li><svg><use href="#i-mobile"/></svg>345 482 0173</li>
      <li><svg><use href="#i-fax"/></svg>345 482 0173</li>
      <li><svg><use href="#i-mail"/></svg>info@novaryn.com.tw</li>
      <li><svg><use href="#i-web"/></svg>www.novaryn.com.tw</li>
    </ul>
  </div>
  <div class="band"></div>
</section>

<!-- Business card, alternate -->
<section class="sheet card card-back">
  <div class="wordmark"><span class="dot"></span>Novaryn</div>
  <div class="abs address lines">7F, 3, Sec. 2, Heping W. Rd.<br>Taipei 10672, Taiwan</div>
  <ul class="abs contact orange-icons">
    <li><svg><use href="#i-phone"/></svg>127 482 0173</li>
    <li><svg><use href="#i-mobile"/></svg>345 482 0173</li>
    <li><svg><use href="#i-fax"/></svg>345 482 0173</li>
    <li><svg><use href="#i-mail"/></svg>info@novaryn.com.tw</li>
    <li><svg><use href="#i-web"/></svg>www.novaryn.com.tw</li>
  </ul>
  <div class="abs sign">
    <div class="name">Wen Liao</div>
    <div class="role">Business Manager</div>
  </div>
  <div class="accent"></div>
</section>

<!-- Letterhead -->
<section class="sheet letterhead">
  <div class="accent left"></div>
  <div class="accent right"></div>
  <div class="wordmark"><span class="dot"></span>Novaryn</div>
  <div class="abs address">7F, 3, Sec. 2, Heping W. Rd<br>Taipei 10672, Taiwan<br><span class="web">www.novaryn.com.tw</span></div>
  <div class="abs divider"></div>
  <ul class="abs contact orange-icons">
    <li><svg><use href="#i-phone"/></svg>127 482 0173</li>
    <li><svg><use href="#i-mobile"/></svg>345 482 0173</li>
    <li><svg><use href="#i-fax"/></svg>345 482 0173</li>
    <li><svg><use href="#i-mail"/></svg>info@novaryn.com.tw</li>
  </ul>
  <div class="abs letter">
    <p class="greeting">Dear Mr. Harlow,</p>
    <p>Lorem ipsum dolor sit amet, consectetur adipiscing elit. Donec orci purus, luctus vitae dignissim eu, iaculis sed purus. Vivamus faucibus, ipsum nec aliquet viverra, leo mauris condimentum ligula, sit amet sagittis enim ligula quis arcu. Nam egestas tortor id nisi porttitor mattis. In tortor ante, ultricies in suscipit a, tempus non massa. Vivamus et auctor mi.</p>
    <p>Fusce vel massa nulla. Phasellus nec eros mauris, et scelerisque orci. Donec malesuada orci vitae nulla accumsan porta a id massa. Quisque accumsan iaculis magna sit amet fringilla. Maecenas consequat, magna eget tincidunt semper, odio nibh rutrum mi, id feugiat ante nisi eu risus. Vestibulum nunc orci, rhoncus a placerat in, ultricies in mi. Cras mattis varius eros, vel fringilla nisi suscipit eget.</p>
    <p>Quisque scelerisque sagittis nulla at porttitor. Mauris a justo et tellus interdum tristique. Sed id augue vitae urna euismod commodo aliquet a quam. Pellentesque arcu velit, cursus et malesuada ut, consequat et diam. Nullam erat sem, rhoncus id ullamcorper vitae, rhoncus et arcu. In ultricies ultricies nulla, ut rutrum nisi iaculis at. Donec eu magna a metus ornare faucibus.</p>
    <p>Fusce aliquet faucibus ultricies. Morbi semper, est id tincidunt gravida, sem arcu adipiscing lacus, ac bibendum nulla leo eu purus. Quisque nec diam sed risus consectetur a ccumsan quis quis nibh. Vestibulum id purus lorem.</p>
    <div class="sign">
      <div class="name">Wen Liao</div>
      <div class="role">Business Manager</div>
    </div>
  </div>
</section>

<!-- Envelope, back -->
<section class="sheet envelope-back">
  <svg class="abs flap" viewBox="0 0 466 80" preserveAspectRatio="none" aria-hidden="true">
    <defs>
      <linearGradient id="flapShade" x1="0" y1="0" x2="0" y2="1">
        <stop offset="0" stop-color="#f4f4f5"/>
        <stop offset="1" stop-color="#e4e4e6"/>
      </linearGradient>
    </defs>
    <path d="M0 0H466L455 62Q450 77 430 77H36Q16 77 11 62Z" fill="url(#flapShade)"/>
    <path d="M11 62Q16 77 36 77H430Q450 77 455 62" fill="none" stroke="#d6d6d8" stroke-width="1"/>
  </svg>
  <div class="wordmark"><span class="dot"></span>Novaryn</div>
  <div class="abs web">www.novaryn.com.tw</div>
</section>

<!-- Envelope, front -->
<section class="sheet envelope-front">
  <div class="accent"></div>
  <div class="wordmark"><span class="dot"></span>Novaryn</div>
  <div class="abs address">7F, 3, Sec. 2, Heping W. Rd<br>Taipei 10672, Taiwan</div>
</section>
</body>
</html>
```